Need a Menu with our Logo and price and food items

Need to develop a Menu page that attracts our customers with our logo we have a basic logo and is very poor I can attach our logo and menu Please help us. The Restaurant menu is attached it must be two pages.must include a little of our history which I will provide very soon.

Industry/Entity Type

Restaurant

Font styles to use
Sans Serif

Requirements
Must have
• Fonda Belvira
3817 Calle Ternura
Cabo Las Nubes
San Juan, PR 000847
tel (787) 413-5276
email: fondabelvirapr@correovela.com
Nice to have
• a google map for directions

```html
<!DOCTYPE html>
<html lang="es">
<head>
<meta charset="utf-8">
<title>Fonda Belvira — Menú</title>
<link href="https://fonts.googleapis.com/css2?family=Cabin+Condensed:wght@400&family=Cabin:wght@400&display=swap" rel="stylesheet">
<style>
  :root {
    --backdrop: #e9e6e1;
    --paper: #fdfdf9;
    --spine: #d6d6d2;
    --ink: #4a4a4a;
    --brand: #3aa7a8;
    --signature: #cfcfca;
  }
  * { margin: 0; padding: 0; box-sizing: border-box; }
  html, body {
    width: 1200px; height: 992px; overflow: hidden;
    background: var(--backdrop);
    font-family: "Cabin", sans-serif;
    color: var(--ink);
  }
  .menu-spread {
    position: absolute; left: 40px; top: 137px;
    width: 1128px; height: 727px;
    display: flex;
    box-shadow: 0 6px 18px rgba(0,0,0,.18);
  }
  .page {
    position: relative;
    width: 564px; height: 100%;
    background: var(--paper);
  }
  .page--back { border-right: 3px solid var(--spine); }
  .brand-name {
    position: absolute; left: 0; right: 0;
    color: var(--brand);
    font-weight: 400;
    text-align: center;
    white-space: nowrap;
    line-height: 1;
  }
  .page--back .brand-name { top: 112px; font-size: 58px; }
  .page--front .brand-name { top: 272px; font-size: 90px; }
  .history {
    position: absolute; left: 36px; top: 243px; width: 500px;
    font-family: "Cabin Condensed", "Cabin", sans-serif;
    font-size: 12px; line-height: 18px;
    text-align: justify;
  }
  .history p { text-indent: 14px; margin-bottom: 14px; }
  .signature {
    position: absolute; left: 370px; top: 552px;
    width: 168px; height: 18px;
    background: linear-gradient(90deg, var(--signature), #bdbdb8);
    border-radius: 9px; opacity: .6;
  }
  .contact {
    position: absolute; left: 0; right: 0; top: 677px;
    text-align: center;
    font-family: "Cabin Condensed", "Cabin", sans-serif;
    font-size: 8px; line-height: 17px;
    font-style: normal;
  }
  .contact em { font-style: italic; }
</style>
</head>
<body>
  <main class="menu-spread">
    <section class="page page--back">
      <h2 class="brand-name">Fonda Belvira</h2>
      <article class="history">
        <p>Desde hacía mucho tiempo mi esposa Elisenda (licenciada en farmacia) y este servidor Tomás Belvira (consultor financiero) soñábamos con algún día tener un restaurante.</p>
        <p>Hace dos años fuimos lo suficientemente atrevido y fundamos Fonda Belvira en Cabo Las Nubes. Tanto mi esposa y yo teníamos vasta experiencia en la cocina y nos encantaba cocinar para nuestras amistades. Nuestros conocimientos crecieron con nuestros viajes a Europa anualmente, muy en especial España e Italia donde se desarrolló nuestra pasión por la cocina mediterránea.</p>
        <p>Todas nuestras recetas de cocina son de nuestra creación y nuestros cocineros que están con nosotros desde el principio siguen las mismas al pie de la letra creando consistencia, lo cual es de gran importancia.</p>
        <p>En otras palabras es como si la familia Belvira los estuviera invitando a cenar a nuestra casa y esa ha sido siempre nuestra intención. Con la ayuda de Dios hemos logrado nuestro sueño y lo compartimos con ustedes. Hemos podido crear una gran fusión de cocina puertorriqueña con mediterránea y lo más importante es contar con el agradecimiento de ustedes, nuestros comensales.</p>
        <p>Esperamos seguir brindando la mejor comida y el mejor servicio.</p>
      </article>
      <div class="signature" role="img" aria-label="Firma manuscrita de Tomás y Elisenda Belvira"></div>
    </section>
    <section class="page page--front">
      <h1 class="brand-name">Fonda Belvira</h1>
      <address class="contact">
        3817 Calle Ternura, Cabo Las Nubes, San Juan, PR 000847 &nbsp;·&nbsp; <em>Phone:</em> (787) 413-5276<br>
        <em>Hours:</em> Thursday to Sunday, 11am - 11pm &nbsp;·&nbsp; <em>E-mail:</em> fondabelvirapr@correovela.com
      </address>
    </section>
  </main>
</body>
</html>
```